Tri-Fold Brochure for Substance Abuse Recovery Center

We are looking to freshen up our tri-fold brochure for our recovery facility. Something that helps convey our message of treatment in the great outdoors. I've included a word document with a mock up.

```html
<!DOCTYPE html>
<html lang="en">
<head>
<meta charset="utf-8">
<title>Cedar Ridge Recovery Center – Tri-Fold Brochure</title>
<link rel="stylesheet" href="https://fonts.googleapis.com/css2?family=Josefin+Sans:wght@400;600;700&family=Nunito+Sans:wght@400;700&display=swap">
<style>
  :root {
    --navy: #2e3d55;
    --orange: #f6a84c;
    --orange-deep: #f29a2e;
    --paper: #f1f2f3;
    --paper-shade: #e4e6e9;
    --ink: #2b3447;
    --stage: #dcdcdc;
    --lake-top: #3a6a9a;
    --lake-bottom: #1f3f66;
    --forest-top: #3f6a36;
    --forest-bottom: #6f8f52;
    --woods-top: #6b7f6a;
    --woods-bottom: #3d4a3c;
  }
  * { box-sizing: border-box; margin: 0; padding: 0; }
  html, body {
    width: 1200px; height: 800px; overflow: hidden;
    background: var(--stage);
    font-family: "Nunito Sans", sans-serif;
    color: var(--ink);
  }
  .brochure { position: relative; width: 1200px; height: 800px; }
  .panel { position: absolute; top: 40px; height: 720px; overflow: hidden; }
  .panel svg.bg, .panel svg.photo { position: absolute; inset: 0; width: 100%; height: 100%; }

  /* Cover */
  .cover { left: 20px; width: 290px; }
  .cover-brand {
    position: absolute; top: 110px; left: 0; width: 100%;
    display: flex; justify-content: center; align-items: center; gap: 10px;
  }
  .cover-brand .dot { width: 22px; height: 22px; border-radius: 50%; background: var(--orange-deep); }
  .cover-brand .name {
    font-family: "Josefin Sans", sans-serif; font-weight: 600; color: var(--navy);
    font-size: 17px; line-height: 1.15; letter-spacing: .5px;
  }
  .cover-brand .name span { display: block; font-size: 11px; letter-spacing: 2.5px; }
  .cover-title {
    position: absolute; top: 178px; left: 0; width: 100%; text-align: center;
    font-family: "Josefin Sans", sans-serif; font-weight: 600; line-height: 1.3;
  }
  .cover-title .main { color: var(--ink); font-size: 17px; display: block; }
  .cover-title .sub { color: var(--orange-deep); font-size: 17px; display: block; }
  .cover-contact {
    position: absolute; top: 618px; left: 0; width: 100%; text-align: center; color: #fff;
    font-family: "Josefin Sans", sans-serif;
  }
  .cover-contact .label { color: var(--orange); font-weight: 700; font-size: 17px; }
  .cover-contact .phone { font-weight: 700; font-size: 19px; margin-top: 4px; }
  .cover-contact .address { font-family: "Nunito Sans", sans-serif; font-size: 10px; margin-top: 6px; }

  /* Inside spread */
  .inside-left { left: 330px; width: 280px; }
  .inside-middle { left: 610px; width: 280px; }
  .inside-right { left: 890px; width: 290px; }

  .quote-mark {
    position: absolute; top: 38px; left: 24px;
    font-family: "Josefin Sans", sans-serif; font-weight: 700; font-size: 64px; line-height: 1; color: var(--navy);
  }
  .testimonial {
    position: absolute; top: 96px; left: 30px; right: 24px;
    font-size: 12px; line-height: 1.45; text-align: justify; color: var(--ink);
  }
  .testimonial cite { display: block; text-align: right; font-style: normal; margin-top: 10px; }

  .body-copy {
    position: absolute; left: 24px; right: 22px;
    font-size: 11.5px; line-height: 1.42; text-align: justify; color: var(--ink);
  }
  .body-copy p + p { margin-top: 24px; }
  .inside-left .body-copy { top: 368px; }

  .section-title {
    font-family: "Josefin Sans", sans-serif; font-weight: 600; font-size: 15px; color: var(--navy);
    margin-bottom: 14px;
  }
  .inside-middle .body-copy { top: 372px; font-size: 11px; }
  .inside-middle .body-copy p + p { margin-top: 10px; }
  .inside-middle .body-copy .section-title + p { margin-top: 0; }
  .inside-middle .body-copy .section-title.gap { margin-top: 26px; }

  .program { position: absolute; top: 98px; left: 18px; right: 20px; }
  .program .section-title { margin-bottom: 10px; }
  .program ul { list-style: none; }
  .program li {
    position: relative; padding-left: 22px; font-size: 11.5px; line-height: 1.3;
    color: var(--ink); margin-bottom: 9px;
  }
  .program li::before {
    content: ""; position: absolute; left: 0; top: 3px; width: 8px; height: 8px; background: var(--navy);
  }

  .activities { position: absolute; top: 402px; left: 32px; right: 20px; }
  .activities .section-title { color: var(--orange-deep); margin-bottom: 8px; }
  .activities .intro { font-size: 11.5px; margin-bottom: 10px; }
  .activities ul { list-style: none; }
  .activities li {
    position: relative; padding-left: 22px; font-size: 12px; line-height: 1.33;
    text-transform: uppercase; color: var(--ink);
  }
  .activities li::before {
    content: ""; position: absolute; left: 2px; top: 7px; width: 3px; height: 3px; border-radius: 50%; background: var(--ink);
  }
</style>
</head>
<body>
<main class="brochure">

  <!-- Front cover -->
  <section class="panel cover">
    <svg class="bg" viewBox="0 0 290 720" preserveAspectRatio="none" aria-hidden="true">
      <rect width="290" height="720" fill="var(--paper)"/>
      <polygon points="0,0 290,0 290,22 0,40" fill="var(--navy)"/>
      <polygon points="0,40 290,22 290,28 0,46" fill="var(--orange-deep)"/>
      <polygon points="0,300 290,218 290,244 0,326" fill="var(--orange-deep)"/>
      <polygon points="0,578 290,514 290,528 0,592" fill="var(--orange)"/>
      <polygon points="0,612 290,548 290,720 0,720" fill="var(--navy)"/>
    </svg>
    <svg class="photo" viewBox="0 0 290 720" preserveAspectRatio="none" role="img" aria-label="Photo of two hikers with backpacks helping each other up a grassy hillside beside a blue lake">
      <defs>
        <linearGradient id="lake" x1="0" y1="0" x2="0" y2="1">
          <stop offset="0" stop-color="var(--lake-top)"/>
          <stop offset="1" stop-color="var(--lake-bottom)"/>
        </linearGradient>
      </defs>
      <polygon points="0,328 290,246 290,512 0,576" fill="url(#lake)"/>
    </svg>
    <div class="cover-brand">
      <span class="dot"></span>
      <div class="name">CEDAR RIDGE<span>RECOVERY CENTER</span></div>
    </div>
    <h1 class="cover-title">
      <span class="main">A Destination for Recovery</span>
      <span class="sub">Inspiring Sobriety &amp; Adventure</span>
    </h1>
    <div class="cover-contact">
      <div class="label">Contact Us 24/7</div>
      <div class="phone">800-555-0147</div>
      <div class="address">12 Hollow Pine Road, Millbrook, WV 25000</div>
    </div>
  </section>

  <!-- Inside left -->
  <section class="panel inside-left">
    <svg class="bg" viewBox="0 0 280 720" preserveAspectRatio="none" aria-hidden="true">
      <rect width="280" height="720" fill="var(--paper)"/>
      <polygon points="0,20 280,20 280,320 0,260" fill="var(--orange)"/>
      <rect width="280" height="22" fill="var(--navy)"/>
      <polygon points="0,22 280,22 280,26 0,30" fill="var(--orange-deep)"/>
      <rect y="690" width="280" height="30" fill="var(--navy)"/>
      <rect y="686" width="280" height="4" fill="var(--orange-deep)"/>
    </svg>
    <div class="quote-mark">&ldquo;</div>
    <blockquote class="testimonial">
      &ldquo;This place is not your typical center. Clients stay busy and active around all day. There are so many outdoor activities that keep them engaged with nature and themselves.&rdquo;
      <cite>-Martha L.</cite>
    </blockquote>
    <div class="body-copy">
      <p>Cedar Ridge is a true destination for recovery. We believe in helping find people their way back, and if it isn&rsquo;t with Cedar Ridge, we will help them find it.</p>
      <p>Located in the mountains, Cedar Ridge is the only center of its kind that allows individuals to heal outdoors in an unmatched environment of support.</p>
      <p>Our programs focus on individualized care covering mental health, medical needs and life skills. We incorporate the Relapse Prevention Program to treat trauma and addiction.</p>
    </div>
  </section>

  <!-- Inside middle -->
  <section class="panel inside-middle">
    <svg class="bg" viewBox="0 0 280 720" preserveAspectRatio="none" aria-hidden="true">
      <rect width="280" height="720" fill="var(--orange)"/>
      <rect width="280" height="22" fill="var(--navy)"/>
      <rect y="690" width="280" height="30" fill="var(--navy)"/>
      <rect y="686" width="280" height="4" fill="var(--orange-deep)"/>
      <rect x="0" width="1.5" height="720" fill="var(--navy)" opacity=".25"/>
    </svg>
    <svg class="photo" viewBox="0 0 280 720" preserveAspectRatio="none" role="img" aria-label="Photo of a calm lake and winding road beside a green wooded hillside">
      <defs>
        <linearGradient id="forest" x1="0" y1="0" x2="0" y2="1">
          <stop offset="0" stop-color="var(--forest-top)"/>
          <stop offset="1" stop-color="var(--forest-bottom)"/>
        </linearGradient>
      </defs>
      <polygon points="0,22 280,22 280,360 0,296" fill="url(#forest)"/>
    </svg>
    <div class="body-copy">
      <h2 class="section-title">Relapse Prevention Program</h2>
      <p>We know the statistics. We want them to change.</p>
      <p>Our Relapse Prevention Program offers an intensive 2 week stabilization program for clients.</p>
      <p>If a patient has been to treatment before, this is the program for them. Our programs have traditional steps to them, with unique individual therapies and recovery options.</p>
      <h2 class="section-title gap">Improvement</h2>
      <p>We want <strong>EVERYONE</strong> to walk out of our facility an improved individual. This includes helping improve credit scores, interviewing skills and family foundations.</p>
    </div>
  </section>

  <!-- Inside right -->
  <section class="panel inside-right">
    <svg class="bg" viewBox="0 0 290 720" preserveAspectRatio="none" aria-hidden="true">
      <rect width="290" height="720" fill="var(--paper)"/>
      <polygon points="0,20 290,20 290,392 0,392" fill="var(--orange)"/>
      <polygon points="0,392 290,392 290,690 0,690" fill="var(--paper-shade)" opacity=".5"/>
      <rect width="290" height="22" fill="var(--navy)"/>
      <polygon points="0,22 290,22 290,34 0,26" fill="var(--orange-deep)"/>
      <rect y="690" width="290" height="30" fill="var(--navy)"/>
      <rect y="686" width="290" height="4" fill="var(--orange-deep)"/>
      <rect x="0" width="1.5" height="720" fill="var(--navy)" opacity=".25"/>
    </svg>
    <svg class="photo" viewBox="0 0 290 720" preserveAspectRatio="none" role="img" aria-label="Photo of a wooden deck railing among tall forest trees">
      <defs>
        <linearGradient id="woods" x1="0" y1="0" x2="0" y2="1">
          <stop offset="0" stop-color="var(--woods-top)"/>
          <stop offset="1" stop-color="var(--woods-bottom)"/>
        </linearGradient>
      </defs>
      <polygon points="60,392 290,236 290,392" fill="url(#woods)"/>
    </svg>
    <div class="program">
      <h2 class="section-title">Our Program</h2>
      <ul>
        <li>A 30 Day Residential Inpatient &amp; Outpatient Treatment.</li>
        <li>Ongoing Recovery Care</li>
        <li>Dialectical Behavioral Therapy</li>
        <li>Emotionally Focused Therapy</li>
        <li>Solution Focused Therapy</li>
        <li>Adventure Therapy</li>
      </ul>
    </div>
    <div class="activities">
      <h2 class="section-title">Activities</h2>
      <p class="intro">These really set us apart!</p>
      <ul>
        <li>Bio Bed</li>
        <li>Acupuncture</li>
        <li>Weekly In-House Salon</li>
        <li>Kayaking</li>
        <li>Hiking</li>
        <li>Fire Pits</li>
        <li>Biking</li>
        <li>Yoga</li>
        <li>Fitness Center</li>
        <li>Pool</li>
        <li>Navigation Ropes Courses</li>
        <li>Zip-Lining</li>
        <li>Rock Climbing</li>
        <li>Games</li>
        <li>Fishing</li>
      </ul>
    </div>
  </section>

</main>
</body>
</html>
```